A start-up named "Corvath Therapeutics" - needs a new PowerPoint design

We need a new PowerPoint Design for an early-stage start-up named "Corvath Therapeutics" seeking to disrupt the current approach towards drug discovery within aging disorders.

We would like to build on Corvath's legacy, the founder of the modern science of genetics, by employing a multidisciplinary approach, experimenting, and providing elderly patients the attention they deserve.

We have selected the suffix "therapeutics" intentionally as it stands for (a medicine) the treatment of disease; the science of healing. Alzheimer’s treatment is a huge, urgent, unmet need:
- Shift from a disease-management system to a preventive medicine system
- Focus on increasing the health span, not only the life span

Target Market(s)

Pharma/ Biotech Executives Medical Institutions Healthcare professionals (MDs, nurses, payors, pharmacists, etc.) Patients

Industry/Entity Type

Healthcare

Other font styles liked:
• Celias

Colors
0054AA
0677BA
7BADD7
CADEEF
E8F1F8
E54698
E96AAD
F1A4CE
F9D9EA
FCEFF6
A7469A
B969AE
D3A5CF
EDDBEB
F8F0F9
6B429C
8869AF
B7A5CE
E3DAEB
F3F0F8

Requirements
Must have
• - differentiate from other companies named after Corvath - differentiate from other Pharma/ Biotech companies
Nice to have
• simplicity/ minimalist logo vivid colors gradient 3D Life-Sciences inspired Simple geometry Balance
Should not have
• mascot/ emblem watermark logo animated ink style nature-inspired inventive typography artistic chaos

```html
<!DOCTYPE html>
<html lang="en">
<head>
<meta charset="utf-8">
<title>Corvath Therapeutics – Presentation Template</title>
<link href="https://fonts.googleapis.com/css2?family=Outfit:wght@400;500;700;800&family=Arimo:wght@400;700&display=swap" rel="stylesheet">
<style>
  :root{
    --sheet:#dcdddd;
    --white:#ffffff;
    --ink:#2b2b2b;
    --grey:#5b5b5b;
    --blue:#1aa9e0;
    --purple:#7b2d8e;
    --violet:#8a2f8f;
    --deep:#3a1d6e;
    --magenta:#b51e8c;
    --bullet:#7b2d8e;
  }
  *{margin:0;padding:0;box-sizing:border-box}
  html,body{width:847px;height:1200px;overflow:hidden;background:var(--sheet)}
  body{position:relative;font-family:"Outfit",sans-serif;color:var(--ink)}

  .slide{position:absolute;width:688px;height:387px;transform:scale(.5228);transform-origin:0 0;
    background:var(--white);overflow:hidden;box-shadow:0 0 0 1.5px #b9b9b9}
  .col-l{left:48.6px}.col-r{left:438.1px}
  .row-1{top:54.9px}.row-2{top:275.5px}.row-3{top:501.9px}.row-4{top:721.5px}.row-5{top:942.6px}

  .abs{position:absolute}
  .art{position:absolute;inset:0;width:100%;height:100%}

  .brand-band{position:absolute;left:0;top:15px;width:310px;height:43px;
    background:linear-gradient(90deg,var(--blue) 0%,#6a3d9a 38%,var(--violet) 100%);
    clip-path:polygon(0 0,287px 0,100% 100%,0 100%)}
  .brand-name{position:absolute;left:36px;top:26px;display:flex;align-items:center;gap:8px;
    color:var(--white);font-weight:500;font-size:15px;white-space:nowrap}
  .brand-mark{width:17px;height:17px;background:var(--white)}

  .heading{position:absolute;font-weight:800;font-size:28px;line-height:34px;letter-spacing:1px;text-transform:uppercase;color:var(--ink)}
  .copy{position:absolute;font-family:"Arimo",sans-serif;font-size:11.5px;line-height:13.6px;color:#333}

  .bullets{position:absolute;list-style:none}
  .bullets li{position:relative;padding-left:32px;font-size:15px;line-height:19px}
  .bullets li::before{content:"";position:absolute;left:0;top:6px;width:8px;height:8px;border-radius:50%;background:var(--bullet)}

  /* slide 1 */
  .cover-art{background:radial-gradient(circle at 70% 35%,#8a3fb0 0%,#4b2a9a 35%,#2a1f7a 65%,#1d1a5e 100%)}
  .cover-panel{position:absolute;left:0;top:25px;width:293px;height:85px;background:var(--white);
    clip-path:polygon(0 0,253px 0,100% 100%,0 100%)}
  .cover-brand{position:absolute;left:46px;top:55px;display:flex;align-items:center;gap:9px;
    font-weight:500;font-size:21px;color:#5a4aa6;white-space:nowrap}
  .cover-brand .brand-mark{width:22px;height:22px;background:#5a4aa6}
  .cover-title{position:absolute;left:43px;top:236px;color:var(--white);font-weight:700;font-size:35px;line-height:50px;letter-spacing:.5px}
  .cover-sub{position:absolute;left:40px;top:329px;color:var(--white);font-weight:800;font-size:19px}

  /* slide 2 */
  .mist{position:absolute;left:250px;top:0;width:438px;height:387px;
    background:linear-gradient(90deg,#ffffff 0%,#e4e6e8 35%,#c5c9cd 70%,#aeb3b8 100%)}
  .chart{position:absolute;left:0;top:0}
  .chart text{font-family:"Arimo",sans-serif}

  /* slide 6 */
  .callout{position:absolute;font-weight:800;font-size:14px;line-height:17px;letter-spacing:.3px}
  .callout.blue{color:var(--blue)}.callout.purple{color:var(--purple)}

  /* slide 7 */
  .dark{background:var(--grey)}
  .dark .heading{color:var(--white)}
  .big-brand{position:absolute;left:50px;top:262px;display:flex;align-items:center;gap:12px;
    color:var(--white);font-weight:500;font-size:27px;white-space:nowrap}
  .big-brand .brand-mark{width:30px;height:30px}
  .ways{position:absolute;left:366px;top:46px;list-style:none;color:var(--white)}
  .ways li{height:64px}
  .ways h3{font-weight:700;font-size:18px;line-height:24px}
  .ways p{padding-left:20px;font-size:11.5px;line-height:14.5px}

  /* slide 8 */
  .pairs{position:absolute;left:42px;top:168px;display:grid;grid-template-columns:93px 93px;row-gap:9.3px}
  .pairs span{position:relative;padding-left:22px;font-size:15px;line-height:19px}
  .pairs span::before{content:"";position:absolute;left:0;top:6px;width:8px;height:8px;border-radius:50%;background:var(--bullet)}

  /* slide 9 */
  .pie-label{font-family:"Outfit",sans-serif;font-size:9px;fill:#fff}
  .legend{position:absolute;left:393px;top:246px;display:grid;grid-template-columns:124px 124px;row-gap:10px}
  .legend span{display:flex;align-items:center;gap:9px;font-size:10.5px;line-height:14px}
  .legend i{width:8px;height:8px;display:block}
</style>
</head>
<body>

<!-- 1 Cover -->
<section class="slide col-l row-1">
  <div class="art cover-art" role="img" aria-label="Purple digital illustration of a human head with a brain, network lines and a virus particle"></div>
  <div class="cover-panel"></div>
  <div class="cover-brand"><span class="brand-mark"></span>Corvath Therapeutics</div>
  <h1 class="cover-title">TITTLE OF<br>YOUR PRESENTATION</h1>
  <p class="cover-sub">Insert the Sub Tittle of Your Presentation</p>
</section>

<!-- 2 Disease management -->
<section class="slide col-r row-1">
  <div class="mist" role="img" aria-label="Soft grey abstract network photograph"></div>
  <div class="brand-band"></div>
  <div class="brand-name"><span class="brand-mark"></span>Corvath Therapeutics</div>
  <h2 class="heading" style="left:38px;top:112px">Disease<br>Management<br>System</h2>
  <p class="copy" style="left:39px;top:224px;width:205px;font-family:'Outfit',sans-serif;font-size:9.5px;line-height:12.2px">Lorem Ipsum is simply dummy text of the printing and typesetting industry. Lorem Ipsum has been the industry's standard dummy text Lorem Ipsum is simply dummy text of the printing and typesetting industry.</p>
  <svg class="chart" width="688" height="387" viewBox="0 0 688 387">
    <rect x="282" y="88" width="357" height="245" fill="#fff"/>
    <g stroke="#333" stroke-width="1">
      <line x1="327" y1="309.9" x2="627" y2="309.9"/><line x1="327" y1="286.8" x2="627" y2="286.8"/>
      <line x1="327" y1="263.7" x2="627" y2="263.7"/><line x1="327" y1="240.6" x2="627" y2="240.6"/>
      <line x1="327" y1="217.5" x2="627" y2="217.5"/><line x1="327" y1="194.4" x2="627" y2="194.4"/>
      <line x1="327" y1="171.3" x2="627" y2="171.3"/><line x1="327" y1="148.2" x2="627" y2="148.2"/>
      <line x1="327" y1="125.1" x2="627" y2="125.1"/>
      <line x1="327" y1="80" x2="327" y2="333" stroke-width="1.4"/>
      <line x1="327" y1="333" x2="650" y2="333" stroke-width="1.4"/>
    </g>
    <g fill="#575757">
      <rect x="340" y="118" width="22" height="215"/>
      <rect x="380.5" y="150.5" width="22" height="182.5"/>
      <rect x="421" y="166.7" width="22" height="166.3"/>
      <rect x="461.5" y="219.8" width="22" height="113.2"/>
      <rect x="502" y="236" width="22" height="97"/>
      <rect x="542.5" y="259" width="22" height="74"/>
      <rect x="583" y="305.3" width="22" height="27.7"/>
    </g>
    <g font-size="10" fill="#222" text-anchor="end">
      <text x="320" y="336">0</text><text x="320" y="313">10</text><text x="320" y="290">20</text>
      <text x="320" y="267">30</text><text x="320" y="244">40</text><text x="320" y="221">50</text>
      <text x="320" y="198">60</text><text x="320" y="175">70</text><text x="320" y="152">80</text>
      <text x="320" y="129">90</text><text x="320" y="106">100</text>
    </g>
    <text x="300" y="205" font-size="11" font-weight="700" fill="#222" text-anchor="middle" transform="rotate(-90 300 205)">Health Span %</text>
    <text x="470" y="361" font-size="12" font-weight="700" fill="#222" text-anchor="middle">Probability a 65 year old</text>
  </svg>
</section>

<!-- 3 Objectives -->
<section class="slide col-l row-2">
  <svg class="art" viewBox="0 0 688 387">
    <polygon points="464,0 688,0 688,387 610,387 395,93" fill="#eeeef1" role="img" aria-label="Photo of an open capsule releasing small granules"/>
    <polygon points="402,0 464,0 395,93 610,387 542,387 327,93" fill="var(--grey)"/>
  </svg>
  <div class="brand-band"></div>
  <div class="brand-name"><span class="brand-mark"></span>Corvath Therapeutics</div>
  <h2 class="heading" style="left:35px;top:92px">Objectives</h2>
  <ul class="bullets" style="left:38px;top:136px;width:320px">
    <li style="margin-bottom:9px">Lorem Ipsum is simply dummy text of the printing and typesetting industry.</li>
    <li style="margin-bottom:14px">Lorem Ipsum is simply dummy text</li>
    <li style="margin-bottom:9px">Lorem Ipsum is simply dummy text of the printing and typesetting industry.</li>
    <li style="margin-bottom:16px">Lorem Ipsum is simply dummy text</li>
    <li>Lorem Ipsum is simply dummy text of the printing and typesetting industry.</li>
  </ul>
</section>

<!-- 4 Science of healing -->
<section class="slide col-r row-2">
  <svg class="art" viewBox="0 0 688 387">
    <defs><linearGradient id="healing" x1="0" y1="0" x2="1" y2="1">
      <stop offset="0" stop-color="#b9b0c4"/><stop offset=".5" stop-color="#7f9aa8"/><stop offset="1" stop-color="#5f8396"/></linearGradient></defs>
    <polygon points="424,0 688,0 688,387 585,387 368,93" fill="url(#healing)" role="img" aria-label="Teal world map backdrop with red virus particles"/>
    <polygon points="362,0 424,0 368,93 585,387 517,387 302,93" fill="var(--grey)"/>
  </svg>
  <div class="brand-band"></div>
  <div class="brand-name"><span class="brand-mark"></span>Corvath Therapeutics</div>
  <h2 class="heading" style="left:41px;top:90px">Science of<br>Healing</h2>
  <ul class="bullets" style="left:41px;top:163px;width:310px">
    <li style="margin-bottom:8px">Lorem Ipsum is simply dummy text of the printing and typesetting industry.</li>
    <li style="margin-bottom:6px">Lorem Ipsum is simply dummy text</li>
  </ul>
  <ul class="bullets" style="left:94px;top:238px">
    <li style="font-size:13px;padding-left:26px;height:20.5px">Lorem Ipsum is simply</li>
    <li style="font-size:13px;padding-left:26px;height:20.5px">Lorem Ipsum is simply dummy text</li>
    <li style="font-size:13px;padding-left:26px;height:20.5px">Lorem Ipsum</li>
    <li style="font-size:13px;padding-left:26px;height:20.5px">Lorem Ipsum</li>
    <li style="font-size:13px;padding-left:26px;height:20.5px">Lorem Ipsum is simply</li>
  </ul>
</section>

<!-- 5 Alzheimer's treatment -->
<section class="slide col-l row-3">
  <svg class="art" viewBox="0 0 688 387">
    <polygon points="347,37 467,0 688,0 688,387 370,387" fill="var(--grey)"/>
    <polygon points="404,62 590,0 688,0 688,387 427,387" fill="#c9c3bd" role="img" aria-label="Photo of an elderly woman assembling a jigsaw puzzle"/>
  </svg>
  <div class="brand-band"></div>
  <div class="brand-name"><span class="brand-mark"></span>Corvath Therapeutics</div>
  <h2 class="heading" style="left:46px;top:78px">Alzheimer’s<br>Treatment</h2>
  <p class="copy" style="left:46px;top:155px;width:290px">Lorem Ipsum is simply dummy text of the printing and typesetting industry. Lorem Ipsum has been the industry's standard dummy text Lorem Ipsum is simply dummy text of the printing and typesetting industry.</p>
  <p class="copy" style="left:46px;top:238px;width:290px">Lorem Ipsum is simply dummy text of the printing and typesetting industry.</p>
  <p class="copy" style="left:46px;top:279px;width:290px">Lorem Ipsum is simply dummy text of the printing and typesetting industry. Lorem Ipsum has been the industry's standard dummy text Lorem Ipsum is simply dummy text of the printing and typesetting industry.</p>
</section>

<!-- 6 Callout circle -->
<section class="slide col-r row-3">
  <div class="brand-band"></div>
  <div class="brand-name"><span class="brand-mark"></span>Corvath Therapeutics</div>
  <svg class="art" viewBox="0 0 688 387">
    <defs><linearGradient id="ring" x1="0" y1="0" x2="1" y2="0">
      <stop offset="0" stop-color="#1aa9e0"/><stop offset="1" stop-color="#8a2f8f"/></linearGradient></defs>
    <circle cx="344" cy="215" r="98" fill="#d8d2cc" role="img" aria-label="Photo of a smiling elderly couple embracing"/>
    <circle cx="344" cy="215" r="105" fill="none" stroke="url(#ring)" stroke-width="5"/>
    <g fill="none" stroke="#9a9a9a" stroke-width="1">
      <polyline points="67,130 192,130 247,175"/>
      <polyline points="434,158 497,113 630,113"/>
      <polyline points="52,278 147,278 242,238"/>
      <polyline points="449,226 524,262 637,262"/>
      <polyline points="110,370 214,370 282,298"/>
      <polyline points="398,305 467,366 570,366"/>
    </g>
    <g stroke="#fff" stroke-width="2">
      <circle cx="247" cy="175" r="6" fill="#1aa9e0"/><circle cx="242" cy="238" r="6" fill="#1aa9e0"/>
      <circle cx="282" cy="298" r="6" fill="#1aa9e0"/><circle cx="434" cy="158" r="6" fill="#8a2f8f"/>
      <circle cx="449" cy="226" r="6" fill="#8a2f8f"/><circle cx="398" cy="305" r="6" fill="#8a2f8f"/>
    </g>
  </svg>
  <p class="callout blue" style="left:67px;top:94px">LOREM<br>IPSUM IS</p>
  <p class="callout purple" style="left:564px;top:64px">LOREM<br>IPSUM IS</p>
  <p class="callout blue" style="left:52px;top:224px">LOREM<br>IPSUM IS</p>
  <p class="callout purple" style="left:569px;top:199px">LOREM<br>IPSUM IS</p>
  <p class="callout blue" style="left:119px;top:319px">LOREM<br>IPSUM IS</p>
  <p class="callout purple" style="left:503px;top:319px">LOREM<br>IPSUM IS</p>
</section>

<!-- 7 Five ways -->
<section class="slide col-l row-4 dark">
  <div class="brand-band"></div>
  <div class="brand-name"><span class="brand-mark"></span>Corvath Therapeutics</div>
  <h2 class="heading" style="left:50px;top:134px;line-height:33px">5 Ways to<br>Avoid Diseases<br>Through</h2>
  <div class="big-brand"><span class="brand-mark" style="background:#fff"></span>Corvath Therapeutics</div>
  <ol class="ways">
    <li><h3>1. Lorem Ipsum Is Simply</h3><p>Lorem Ipsum is simply dummy text of<br>the printing and typesetting industry.</p></li>
    <li><h3>2. Lorem Ipsum Is Simply</h3><p>Lorem Ipsum is simply dummy text of<br>the printing and typesetting industry.</p></li>
    <li><h3>3. Lorem Ipsum Is Simply</h3><p>Lorem Ipsum is simply dummy text of<br>the printing and typesetting industry.</p></li>
    <li><h3>4. Lorem Ipsum Is Simply</h3><p>Lorem Ipsum is simply dummy text of<br>the printing and typesetting industry.</p></li>
    <li><h3>5. Lorem Ipsum Is Simply</h3><p>Lorem Ipsum is simply dummy text of<br>the printing and typesetting industry.</p></li>
  </ol>
</section>

<!-- 8 Health span -->
<section class="slide col-r row-4">
  <svg class="art" viewBox="0 0 688 387">
    <defs><linearGradient id="clinic" x1="0" y1="0" x2="1" y2="1">
      <stop offset="0" stop-color="#eef6fb"/><stop offset=".55" stop-color="#a9d8ef"/><stop offset="1" stop-color="#5fb6e0"/></linearGradient></defs>
    <polygon points="467,112 688,112 688,387 392,387 334,275" fill="url(#clinic)" role="img" aria-label="Photo of an alarm clock inside a stethoscope on a blue surface"/>
    <polygon points="519,0 559,0 334,275 392,387 324,387 267,275" fill="var(--grey)"/>
  </svg>
  <div class="brand-band"></div>
  <div class="brand-name"><span class="brand-mark"></span>Corvath Therapeutics</div>
  <h2 class="heading" style="left:42px;top:90px">Health Span<br>Lorem Ipsum Is</h2>
  <div class="pairs">
    <span>Age</span><span>Age</span><span>Gender</span><span>Gender</span>
    <span>Age</span><span>Age</span><span>Gender</span><span>Gender</span>
    <span>Age</span><span>Age</span><span>Gender</span><span>Gender</span>
    <span>Age</span><span>Age</span>
  </div>
</section>

<!-- 9 Pie chart -->
<section class="slide col-l row-5">
  <div class="brand-band"></div>
  <div class="brand-name"><span class="brand-mark"></span>Corvath Therapeutics</div>
  <h2 class="heading" style="left:50px;top:98px;font-size:27px;line-height:33px">Lorem Ipsum Is<br>Simply Dummy<br>Text of the<br>Printing and<br>Typesetting<br>Industry.</h2>
  <p style="position:absolute;left:50px;top:310px;font-size:11.5px;line-height:14.5px">Lorem Ipsum is simply dummy text of<br>the printing and typesetting industry.</p>
  <svg class="art" viewBox="0 0 688 387">
    <g transform="translate(469 133)">
      <path d="M148 0 A148 64 0 0 1 107.9 43.8 L107.9 71.8 A148 64 0 0 0 148 28 Z" fill="#222"/>
      <path d="M107.9 43.8 A148 64 0 0 1 -18.5 63.5 L-18.5 91.5 A148 64 0 0 0 107.9 71.8 Z" fill="#5a1f6a"/>
      <path d="M-18.5 63.5 A148 64 0 0 1 -114 40.8 L-114 68.8 A148 64 0 0 0 -18.5 91.5 Z" fill="#c49a00"/>
      <path d="M-114 40.8 A148 64 0 0 1 -137.6 23.6 L-137.6 51.6 A148 64 0 0 0 -114 68.8 Z" fill="#1f1f55"/>
      <path d="M-137.6 23.6 A148 64 0 0 1 -148 0 L-148 28 A148 64 0 0 0 -137.6 51.6 Z" fill="#c2561a"/>
      <path d="M0 0 L0 -64 A148 64 0 0 1 101.3 -46.7 Z" fill="#b51e8c"/>
      <path d="M0 0 L101.3 -46.7 A148 64 0 0 1 107.9 43.8 Z" fill="#3a3a3a"/>
      <path d="M0 0 L107.9 43.8 A148 64 0 0 1 -18.5 63.5 Z" fill="#7b2d8e"/>
      <path d="M0 0 L-18.5 63.5 A148 64 0 0 1 -114 40.8 Z" fill="#f2d40f"/>
      <path d="M0 0 L-114 40.8 A148 64 0 0 1 -137.6 23.6 Z" fill="#2d2d78"/>
      <path d="M0 0 L-137.6 23.6 A148 64 0 0 1 -137.6 -23.6 Z" fill="#f07c22"/>
      <path d="M0 0 L-137.6 -23.6 A148 64 0 0 1 -36.8 -62 Z" fill="#5b2d7e"/>
      <path d="M0 0 L-36.8 -62 A148 64 0 0 1 -18.5 -63.5 Z" fill="#e88a8f"/>
      <path d="M0 0 L-18.5 -63.5 A148 64 0 0 1 0 -64 Z" fill="#4db4e6"/>
    </g>
    <g class="pie-label">
      <text x="437" y="80" fill="#333" style="fill:#333">2%</text><text x="457" y="80" style="fill:#333">2%</text>
      <text x="389" y="102">15%</text><text x="487" y="98">12%</text><text x="546" y="127">25%</text>
      <text x="352" y="130">12%</text><text x="359" y="167">5%</text><text x="435" y="180" style="fill:#333">12%</text>
    </g>
  </svg>
  <div class="legend">
    <span><i style="background:#4db4e6"></i>Lorem Ipsum</span><span><i style="background:#f2d40f"></i>Lorem Ipsum</span>
    <span><i style="background:#e88a8f"></i>Lorem Ipsum</span><span><i style="background:#7b2d8e"></i>Lorem Ipsum</span>
    <span><i style="background:#5b2d7e"></i>Lorem Ipsum</span><span><i style="background:#3a3a3a"></i>Lorem Ipsum</span>
    <span><i style="background:#f07c22"></i>Lorem Ipsum</span><span><i style="background:#b51e8c"></i>Lorem Ipsum</span>
    <span><i style="background:#2d2d78"></i>Lorem Ipsum</span>
  </div>
</section>

</body>
</html>
```